Concierge Dental / Medical Supply Ordering Business - Sleek, Efficient, Professional, Elite

www.brixtonfaymedical.example - example website.

We are a concierge supply ordering business for medical and dental that provide DSO price savings on supplies while maintaining business autonomy and independence.

We want a very simple website that looks very professional says what we do and gives a very simple method to contact us & sign up as above.

Target Market(s)

Independent Dental and Medical Practices

Industry/Entity Type

Dental and Medical - healthcare

Coding

Coded - Design and coding required

Number of Pages Required

3 page

Font styles to use
Sans Serif

Colors
0054AA
0677BA
7BADD7
CADEEF
E8F1F8

Requirements
Must have
• Simple contact page, sleek efficient design, uncomplicated.
Nice to have
• Sign up page vs just a contact page.
Should not have
• Lots of pages, hard to navigate,

```html
<!DOCTYPE html>
<html lang="en">
<head>
<meta charset="utf-8">
<title>Brixton Fay Supply</title>
<link rel="stylesheet" href="https://fonts.googleapis.com/css2?family=Poppins:wght@600;700&family=Roboto:wght@400;500;700&display=swap">
<style>
:root{
  --blue:#0a9be3;
  --blue-bright:#0aa6f0;
  --blue-deep:#0677ba;
  --ink:#111;
  --black:#000;
  --dark:#2b2b2b;
  --white:#fff;
  --muted:#6b6b6b;
  --light:#cadeef;
}
*{box-sizing:border-box;margin:0;padding:0}
html,body{width:1200px;height:3561px;overflow:hidden}
body{position:relative;font-family:'Roboto',sans-serif;background:var(--white);color:var(--ink)}
.abs{position:absolute}
.head-font{font-family:'Poppins',sans-serif;font-weight:700}

/* header */
.site-header{left:0;top:0;width:1200px;height:133px;background:var(--black)}
.topbar{left:491px;top:0;width:709px;height:50px;background:linear-gradient(90deg,var(--blue-bright),var(--blue-deep));clip-path:polygon(0 0,100% 0,100% 100%,34px 100%)}
.social-top{top:9px;width:32px;height:32px;border:2px solid var(--white);border-radius:50%}
.call{left:795px;top:11px;color:var(--white);font-size:15px;font-weight:700}
.call b{font-size:20px}
.brand{left:148px;top:30px;display:flex;align-items:center;gap:10px}
.brand-mark{width:26px;height:26px;background:var(--blue)}
.brand-name{font-family:'Roboto',sans-serif;font-weight:700;font-size:18px;color:var(--white)}
.nav a{position:absolute;top:84px;color:var(--white);font-weight:700;font-size:14px;text-decoration:none}
.nav a.active{color:var(--blue-bright)}
.nav a.active::after{content:"";position:absolute;left:0;right:0;bottom:-6px;height:3px;background:var(--blue-bright)}
.btn{display:flex;align-items:center;justify-content:center;gap:6px;border-radius:24px;font-weight:700;font-size:14px;color:var(--white);background:var(--blue-bright)}
.btn .dot{width:12px;height:12px;border-radius:50%;background:var(--white)}

/* hero */
.hero{left:0;top:133px;width:1200px;height:706px;background:linear-gradient(120deg,#2d4a6b 0%,#8a8f96 45%,#cfd3d8 70%,#5b6f86 100%)}
.hero-panel{left:375px;top:380px;width:452px;height:267px;background:rgba(80,80,80,.72);border-radius:8px;text-align:center}
.hero-title{margin-top:20px;font-size:53px;line-height:68px;color:var(--white)}
.scroll{left:553px;top:792px;width:94px;height:94px;border-radius:50%;background:var(--white);border:3px solid var(--dark);box-shadow:0 0 0 3px var(--white)}

/* practice */
.practice{left:0;top:839px;width:1200px;height:1090px;background:radial-gradient(ellipse at 50% 55%,#4a4a4a 0%,#2a2a2a 60%,#1a1a1a 100%)}
.section-title{font-size:55px;text-align:center;color:var(--white)}
.rule{height:3px;background:var(--blue-bright)}
.frame{width:213px;height:213px;border:8px solid var(--blue-bright);border-radius:10px}
.area-title{font-family:'Poppins',sans-serif;font-weight:600;font-size:38px;color:var(--white)}
.area-text{font-size:15px;line-height:25.7px;color:#e9e9e9;text-align:justify}

/* about */
.about-title{left:112px;top:2030px;font-size:55px}
.about-text{left:112px;width:453px;font-size:15px;line-height:25.7px;color:var(--muted);text-align:justify}
.about-photo{left:646px;top:2046px;width:441px;height:509px;border-radius:14px;background:linear-gradient(160deg,#e5eef7,#9cc3e6 50%,#3a7fc4)}

/* contact band */
.band-photo{left:0;top:2679px;width:1200px;height:396px;background:linear-gradient(100deg,#cfd6de,#8a98a8 40%,#3b4654)}
.band-blue{left:0;top:2679px;width:1200px;height:396px;background:linear-gradient(90deg,#0aa6f0,#0a8fd8);clip-path:polygon(556px 0,1200px 0,1200px 100%,691px 100%)}
.band-text{font-size:17px;line-height:25px;color:var(--white);text-align:center}

/* footer */
.site-footer{left:0;top:3075px;width:1200px;height:486px;background:linear-gradient(180deg,#262626,#3a3a3a)}
.f-head{font-size:19px;font-weight:500;color:var(--white)}
.field{background:var(--white);padding:10px 18px;font-size:13px;color:#666}
.links a{position:absolute;left:671px;font-size:15px;color:var(--white);text-decoration:none}
.links a::before{content:"»";position:absolute;left:-21px;color:var(--blue-bright)}
.c-item{font-size:15px;line-height:24px;color:var(--white)}
.soc{width:32px;height:32px;border-radius:50%}
</style>
</head>
<body>

<header class="abs site-header">
  <div class="abs topbar"></div>
  <span class="abs social-top" style="left:643px"></span>
  <span class="abs social-top" style="left:680px"></span>
  <span class="abs social-top" style="left:717px"></span>
  <svg class="abs" style="left:795px;top:16px" width="16" height="16" viewBox="0 0 24 24"><path fill="#fff" d="M6.6 10.8a15.1 15.1 0 0 0 6.6 6.6l2.2-2.2c.3-.3.7-.4 1-.2 1.1.4 2.3.6 3.6.6.6 0 1 .4 1 1V20c0 .6-.4 1-1 1A17 17 0 0 1 3 4c0-.6.4-1 1-1h3.5c.6 0 1 .4 1 1 0 1.3.2 2.5.6 3.6.1.3 0 .7-.2 1z"/></svg>
  <div class="abs call" style="left:828px">Call us Today : <b>+1 888 888 8888</b></div>
  <div class="abs brand"><span class="brand-mark"></span><span class="brand-name">BrixtonFaySupply</span></div>
  <nav class="nav">
    <a class="active" style="left:470px">HOME</a>
    <a style="left:543px">ABOUT US</a>
    <a style="left:646px">SERVICES</a>
    <a style="left:745px">PRICING</a>
    <a style="left:835px">CONTACT US</a>
  </nav>
  <div class="abs btn" style="left:947px;top:72px;width:142px;height:44px">GET A QUOTE</div>
</header>

<section class="abs hero" role="img" aria-label="Medical team meeting around a table"></section>
<div class="abs hero-panel">
  <h1 class="head-font hero-title">Brixton Fay<br>Supply</h1>
  <div class="abs btn" style="left:145px;top:174px;width:160px;height:43px">GET STARTED <span class="dot"></span></div>
</div>

<section class="abs practice">
  <h2 class="abs head-font section-title" style="left:0;width:1200px;top:108px">Areas of Practice</h2>
  <div class="abs rule" style="left:574px;top:196px;width:91px"></div>

  <div class="abs frame" style="left:200px;top:238px;background:linear-gradient(135deg,#6d8e4a,#c99a6a)" role="img" aria-label="Volunteers handing out supplies"></div>
  <h3 class="abs area-title" style="left:471px;top:250px">Distribution</h3>
  <p class="abs area-text" style="left:471px;top:306px;width:529px">Lorem ipsum dolor sit amet, consectetur adipiscing elit, sed do eiusmod tempor incididunt ut labore et dolore magna aliqua. Ut enim ad minim veniam, quis nostrud exercitation ullamco laboris nisi ut aliquip ex ea commodo consequat. Duis aute irure dolor in reprehenderit in voluptate velit esse cillum dolore eu fugiat nulla pariatur. Excepteur sint occaecat cupidatat non proident</p>

  <div class="abs frame" style="left:794px;top:487px;background:linear-gradient(135deg,#e7ecf1,#7aa3c9)" role="img" aria-label="Scientists working in a laboratory"></div>
  <h3 class="abs area-title" style="left:209px;width:526px;text-align:right;top:498px">Pharma</h3>
  <p class="abs area-text" style="left:209px;top:554px;width:526px;text-align-last:right">Lorem ipsum dolor sit amet, consectetur adipiscing elit, sed do eiusmod tempor incididunt ut labore et dolore magna aliqua. Ut enim ad minim veniam, quis nostrud exercitation ullamco laboris nisi ut aliquip ex ea commodo consequat. Duis aute irure dolor in reprehenderit in voluptate velit esse cillum dolore eu fugiat nulla pariatur. Excepteur sint occaecat cupidatat non proident</p>

  <div class="abs frame" style="left:200px;top:751px;background:linear-gradient(135deg,#9fb6c8,#e6eef4 50%,#6f8aa3)" role="img" aria-label="Clean equipment production hall"></div>
  <h3 class="abs area-title" style="left:471px;top:733px">Capital Equipment</h3>
  <p class="abs area-text" style="left:471px;top:788px;width:529px">Lorem ipsum dolor sit amet, consectetur adipiscing elit, sed do eiusmod tempor incididunt ut labore et dolore magna aliqua. Ut enim ad minim veniam, quis nostrud exercitation ullamco laboris nisi ut aliquip ex ea commodo consequat. Duis aute irure dolor in reprehenderit in voluptate velit esse cillum dolore eu fugiat nulla pariatur. Excepteur sint occaecat cupidatat non proident</p>
</section>

<div class="abs scroll">
  <svg width="88" height="88" viewBox="0 0 88 88"><rect x="34" y="18" width="20" height="32" rx="10" fill="none" stroke="#222" stroke-width="2.5"/><line x1="44" y1="25" x2="44" y2="31" stroke="#222" stroke-width="2.5"/><path d="M37 56l7 6 7-6M37 63l7 6 7-6" fill="none" stroke="#222" stroke-width="2.5"/></svg>
</div>

<section>
  <h2 class="abs head-font about-title">About Us</h2>
  <div class="abs rule" style="left:112px;top:2121px;width:130px"></div>
  <p class="abs about-text" style="top:2160px">Lorem ipsum dolor sit amet, consectetur adipiscing elit, sed do eiusmod tempor incididunt ut labore et dolore magna aliqua. Ut enim ad minim veniam, quis nostrud exercitation ullamco laboris nisi ut aliquip ex ea commodo consequat. Duis aute irure dolor in reprehenderit in voluptate velit esse cillum dolore eu fugiat nulla pariatur. Excepteur sint occaecat cupidatat non proident, sunt in culpa qui officia deserunt mollit anim id est laborum.</p>
  <p class="abs about-text" style="top:2366px">Lorem ipsum dolor sit amet, consectetur adipiscing elit, sed do eiusmod tempor incididunt ut labore et dolore magna aliqua. Ut enim ad minim veniam, quis nostrud exercitation ullamco laboris nisi ut aliquip ex ea commodo consequat. Duis aute irure dolor in reprehenderit in voluptate velit esse cillum dolore</p>
  <div class="abs btn" style="left:112px;top:2515px;width:159px;height:42px">LEARN MORE <span class="dot"></span></div>
  <div class="abs about-photo" role="img" aria-label="Lab technician in protective suit handling samples"></div>
</section>

<section>
  <div class="abs band-photo" role="img" aria-label="Doctors reviewing documents at a meeting"></div>
  <div class="abs band-blue"></div>
  <h2 class="abs head-font section-title" style="left:717px;width:400px;top:2752px">Get in Touch</h2>
  <div class="abs" style="left:852px;top:2843px;width:91px;height:3px;background:var(--white)"></div>
  <p class="abs band-text" style="left:660px;width:515px;top:2866px">For all questions, inquires regarding our services, or assistance in referring someone to us. Please contact us below.</p>
  <div class="abs btn" style="left:839px;top:2935px;width:159px;height:43px;background:var(--white);color:var(--blue-bright)">
    <svg width="13" height="13" viewBox="0 0 14 14"><rect x="1" y="2.5" width="12" height="10.5" rx="1" fill="none" stroke="#0aa6f0" stroke-width="1.6"/><line x1="1" y1="6" x2="13" y2="6" stroke="#0aa6f0" stroke-width="1.6"/></svg>BOOK NOW</div>
</section>

<footer class="abs site-footer">
  <h4 class="abs f-head" style="left:111px;top:80px">REQUEST A QUOTE</h4>
  <div class="abs field" style="left:112px;top:127px;width:234px;height:37px">First name</div>
  <div class="abs field" style="left:354px;top:127px;width:234px;height:37px">Last name</div>
  <div class="abs field" style="left:112px;top:175px;width:234px;height:38px">Email</div>
  <div class="abs field" style="left:354px;top:175px;width:234px;height:38px">Phone number</div>
  <div class="abs field" style="left:112px;top:226px;width:476px;height:74px">Message</div>
  <div class="abs btn" style="left:112px;top:318px;width:133px;height:44px;font-size:15px">SUBMIT</div>

  <h4 class="abs f-head" style="left:650px;top:80px">QUICK LINKS</h4>
  <div class="links">
    <a style="top:116px">Home</a><a style="top:146px">About Us</a><a style="top:176px">Why us?</a>
    <a style="top:206px">Blog</a><a style="top:236px">Partners</a><a style="top:266px">Contact Us</a>
  </div>

  <h4 class="abs f-head" style="left:847px;top:80px">CONTACT US</h4>
  <svg class="abs" style="left:851px;top:124px" width="12" height="16" viewBox="0 0 12 16"><path d="M6 0a6 6 0 0 0-6 6c0 4.5 6 10 6 10s6-5.5 6-10a6 6 0 0 0-6-6zm0 8.5A2.5 2.5 0 1 1 6 3.5a2.5 2.5 0 0 1 0 5z" fill="#0aa6f0"/></svg>
  <p class="abs c-item" style="left:880px;top:122px">Lorem ipsum dolor sit amet,<br>consectetur adipiscing</p>
  <svg class="abs" style="left:850px;top:200px" width="10" height="16" viewBox="0 0 10 16"><rect x="1" y="1" width="8" height="14" rx="1.5" fill="none" stroke="#0aa6f0" stroke-width="1.6"/></svg>
  <p class="abs c-item" style="left:880px;top:196px">+1 888 888 8888</p>
  <svg class="abs" style="left:847px;top:253px" width="18" height="13" viewBox="0 0 18 13"><rect x="1" y="1" width="16" height="11" fill="none" stroke="#0aa6f0" stroke-width="1.5"/><path d="M1 1l8 6 8-6" fill="none" stroke="#0aa6f0" stroke-width="1.5"/></svg>
  <p class="abs c-item" style="left:884px;top:249px">info@companyname.com</p>

  <h4 class="abs f-head" style="left:650px;top:338px">STAY CONNECTED :</h4>
  <span class="abs soc" style="left:850px;top:332px;background:#3b5fc4"></span>
  <span class="abs soc" style="left:889px;top:332px;background:#c72fb0"></span>
  <span class="abs soc" style="left:927px;top:332px;background:#d8262a"></span>

  <div class="abs" style="left:111px;top:399px;width:978px;height:1px;background:#555"></div>
  <p class="abs" style="left:0;width:1200px;top:428px;text-align:center;color:var(--white);font-size:16px">© 2023 Company name &nbsp;| All Rights Reserved | Terms and Conditions</p>
</footer>

</body>
</html>
```